Dog grooming business card
This is a business card for m dog grooming business like it say above.
In the priorities box below I will have the text that I want on the card.

Industry/Entity Type

Business

Colors

Designer to choose colors to be used in the design.

Requirements
Must have
• My logo and the insurance stamp must be on the card.

Text it must have :

Professional grooming services
Email: lunabrisk@mailvane.net
Text or call 1 705 318 6642
TKV certified/member
Pet first aid certified
Next appointment ___________________________________
Nice to have
• Greens to match my logo

```html
<!DOCTYPE html>
<html lang="en">
<head>
<meta charset="utf-8">
<title>Luna Brisk – Grooming Business Card</title>
<link rel="stylesheet" href="https://fonts.googleapis.com/css2?family=Open+Sans:wght@400;700;800&family=Sansita:ital,wght@1,700&display=swap">
<style>
  :root {
    --page: #e9e9e7;
    --card: #ffffff;
    --ink: #2b2b2b;
    --ink-soft: #555555;
    --green: #7fb13a;
    --green-pale: #dbe9c4;
    --green-line: #c9dca6;
    --badge: #d7e6f5;
    --badge-edge: #8fb3da;
  }
  * { box-sizing: border-box; margin: 0; padding: 0; }
  html, body {
    width: 1200px; height: 873px; overflow: hidden;
    background: var(--page);
    font-family: "Open Sans", Arial, sans-serif;
    color: var(--ink);
  }
  .stage {
    width: 1200px; height: 873px;
    display: flex; justify-content: center; align-items: center; gap: 70px;
  }
  .card {
    width: 340px; height: 580px;
    background: var(--card);
    box-shadow: 0 2px 10px rgba(0,0,0,.12);
    position: relative;
    padding: 40px 32px;
    display: flex; flex-direction: column; align-items: center;
  }

  /* Front */
  .brand {
    margin-top: 40px;
    display: flex; align-items: center; gap: 12px;
  }
  .brand-dot {
    width: 26px; height: 26px; border-radius: 50%;
    background: var(--green);
  }
  .brand-name {
    font-size: 36px; font-weight: 700; color: var(--green);
    letter-spacing: .5px;
  }
  .tagline {
    margin-top: 70px;
    font-size: 19px; font-weight: 800; text-align: center; line-height: 1.25;
  }
  .contact {
    margin-top: 22px; list-style: none; text-align: center;
    font-size: 17px; line-height: 1.4; color: var(--ink-soft);
  }
  .flourish {
    position: absolute; left: 60px; right: 60px; bottom: 60px; height: 54px;
    background: linear-gradient(90deg, transparent, var(--green-pale) 25%, var(--green-pale) 75%, transparent);
    border-radius: 27px;
  }

  /* Back */
  .reminder-title {
    align-self: flex-start;
    font-family: "Sansita", Georgia, serif; font-style: italic; font-weight: 700;
    font-size: 24px; margin-top: 6px;
  }
  .rule { width: 100%; height: 2px; background: var(--green-line); margin: 12px 0; }
  .weekdays {
    width: 100%; display: flex; justify-content: space-between;
    font-weight: 800; font-size: 14px; margin-top: 6px;
  }
  .dates {
    width: 100%; margin-top: 18px;
    display: grid; grid-template-columns: repeat(7, 1fr); row-gap: 12px;
    font-weight: 800; font-size: 16px; text-align: center;
  }
  .months-row {
    width: 100%; display: flex; align-items: center; gap: 10px; margin-top: 14px;
  }
  .months {
    flex: 1; display: grid; grid-template-columns: repeat(6, 1fr); row-gap: 8px;
    font-weight: 800; font-size: 13px; text-align: center;
  }
  .partner-badge {
    width: 46px; height: 26px; border-radius: 4px;
    background: var(--badge); border: 1.5px solid var(--badge-edge);
  }
  .time-line {
    align-self: flex-start; margin-top: 14px;
    font-size: 15px; color: var(--ink-soft);
  }
  .blank { display: inline-block; width: 44px; border-bottom: 1.5px solid var(--ink-soft); }
</style>
</head>
<body>
<main class="stage">
  <section class="card card-front">
    <div class="brand">
      <span class="brand-dot"></span>
      <span class="brand-name">Luna Brisk</span>
    </div>
    <h1 class="tagline">Professional grooming<br>services</h1>
    <ul class="contact">
      <li>lunabrisk@mailvane.net</li>
      <li>Text or call: 1 705 318 6642</li>
      <li>TKV certified/member</li>
      <li>Pet first aid certified</li>
    </ul>
    <div class="flourish" role="img" aria-label="Green decorative swirl flourish"></div>
  </section>

  <section class="card card-back">
    <h2 class="reminder-title">Appointment reminder</h2>
    <div class="rule"></div>
    <div class="weekdays"><span>MON</span><span>TUE</span><span>WEDS</span><span>THURS</span><span>FRI</span></div>
    <div class="rule"></div>
    <div class="dates">
      <span>1</span><span>2</span><span>3</span><span>4</span><span>5</span><span>6</span><span>7</span>
      <span>8</span><span>9</span><span>10</span><span>11</span><span>12</span><span>13</span><span>14</span>
      <span>15</span><span>16</span><span>17</span><span>18</span><span>19</span><span>20</span><span>21</span>
      <span>22</span><span>23</span><span>24</span><span>25</span><span>26</span><span>27</span><span>28</span>
      <span>29</span><span>30</span><span>31</span>
    </div>
    <div class="rule"></div>
    <div class="months-row">
      <div class="months">
        <span>JAN</span><span>FEB</span><span>MAR</span><span>APR</span><span>MAY</span><span>JUN</span>
        <span>JUL</span><span>AUG</span><span>SEP</span><span>OCT</span><span>NOV</span><span>DEC</span>
      </div>
      <div class="partner-badge" role="img" aria-label="Insurance stamp"></div>
    </div>
    <div class="rule"></div>
    <p class="time-line">At <span class="blank"></span> : <span class="blank"></span> am/pm</p>
  </section>
</main>
</body>
</html>
```